Original and striking logo and label design for a young handcrafted dry gin

I am starting a small artisan distillery venture to produce gin. The brand will be called Velmora which means sunset. As my product is going to be new, modest and small-scale, but at the same time of high quality, I need to differentiate it through its packaging. As within my possibilities I have to resort to standard bottles on the market, it is important to have an original and different label. I want to be able to mark the premium character but at the same time handmade, between vintage or minimalist style (I have not decided yet which would be better). In the annex there is an "Inspiration.rar" file with images of other inspiring gin brands, which are a good example of the sense of excellence that the project must convey. I have already made some label models myself, but I am not satisfied, which I attach. Additionally, I enclose two models of bottles that interest me, with which the label should be able to adapt to both models. Please, if you are not at least at the level of the inspiration images, do not try to propose your model.

Target Market(s)

The product is mainly aimed at young people who appreciate high-quality beverages and who value an artisanal and sustainable product.

Logo Text

Velmora

Font styles to use
Serif
Decorative
Script

Requirements
Must have
• Reference to the Portuguese sunset (at sea). Reference to what is handcrafted; Portuguese. They must include the following slogan: "Distilled in the glow of the
Portuguese Sunset". The label should allow the following information to be completed by hand: Date distilled; Distiller; Bottle No.; Batch No.

```html
<!DOCTYPE html>
<html lang="en">
<head>
<meta charset="utf-8">
<title>Velmora Gin Label</title>
<link href="https://fonts.googleapis.com/css2?family=Rye&family=Patrick+Hand&family=Patrick+Hand+SC&display=swap" rel="stylesheet">
<style>
  :root {
    --page: #f3f3f1;
    --label: #2a2a2a;
    --plaque: #151515;
    --panel: #3a3a3a;
    --cream: #f1ede3;
    --amber: #d9822b;
    --sun: #f2a324;
    --ornament: #8a8780;
  }
  html, body {
    margin: 0;
    padding: 0;
    overflow: hidden;
    background: var(--page);
  }
  .canvas {
    position: relative;
    width: 1200px;
    height: 1200px;
    overflow: hidden;
    background: var(--page);
  }
  .label {
    position: absolute;
    left: 160px;
    top: 60px;
    width: 880px;
    height: 1080px;
    background: var(--label);
  }
  .label-frame {
    position: absolute;
    left: 0;
    top: 0;
  }
  .category {
    position: absolute;
    left: 0;
    width: 100%;
    top: 22px;
    margin: 0;
    text-align: center;
    font-family: "Patrick Hand SC", cursive;
    font-size: 38px;
    line-height: 40px;
    letter-spacing: 1px;
    color: var(--cream);
    font-weight: 400;
  }
  .ornament {
    position: absolute;
    left: 150px;
    width: 580px;
    background: linear-gradient(180deg, rgba(138,135,128,0.35), rgba(138,135,128,0.55));
    border-radius: 6px;
  }
  .ornament-top { top: 150px; height: 120px; }
  .ornament-bottom { top: 770px; height: 130px; }
  .sun-mark {
    position: absolute;
    left: 412px;
    top: 280px;
    width: 56px;
    height: 56px;
    border-radius: 50%;
    background: var(--sun);
  }
  .rule {
    position: absolute;
    left: 165px;
    width: 550px;
    height: 4px;
    background: var(--cream);
  }
  .rule-top { top: 352px; }
  .rule-bottom { top: 538px; }
  .brand-name {
    position: absolute;
    left: 0;
    width: 100%;
    top: 370px;
    margin: 0;
    text-align: center;
    font-family: "Rye", serif;
    font-weight: 400;
    font-size: 90px;
    line-height: 150px;
    color: var(--cream);
  }
  .handcrafted {
    position: absolute;
    left: 0;
    width: 100%;
    top: 560px;
    margin: 0;
    text-align: center;
    font-family: "Patrick Hand SC", cursive;
    font-size: 40px;
    line-height: 48px;
    color: var(--amber);
  }
  .slogan {
    position: absolute;
    left: 0;
    width: 100%;
    top: 618px;
    margin: 0;
    text-align: center;
    font-family: "Patrick Hand", cursive;
    font-size: 44px;
    line-height: 56px;
    color: var(--cream);
  }
  .fill-in {
    position: absolute;
    left: 230px;
    width: 420px;
    top: 966px;
    margin: 0;
    display: grid;
    grid-template-columns: 1fr 1fr;
    column-gap: 24px;
    row-gap: 14px;
    font-family: "Patrick Hand", cursive;
    font-size: 24px;
    line-height: 28px;
    color: var(--cream);
  }
  .fill-in-field {
    display: flex;
    align-items: flex-end;
    gap: 6px;
    white-space: nowrap;
  }
  .fill-in-line {
    flex: 1;
    border-bottom: 2px solid var(--cream);
    margin-bottom: 5px;
  }
  .spec {
    position: absolute;
    top: 1000px;
    margin: 0;
    font-family: "Patrick Hand", cursive;
    font-size: 38px;
    line-height: 44px;
    color: var(--cream);
  }
  .spec-abv { left: 40px; }
  .spec-volume { right: 40px; }
</style>
</head>
<body>
<div class="canvas">
  <section class="label">
    <svg class="label-frame" width="880" height="1080" viewBox="0 0 880 1080" aria-hidden="true">
      <path d="M108 70 H772 V100 H802 V924 H772 V954 H108 V924 H78 V100 H108 Z"
            fill="var(--cream)"/>
      <path d="M118 80 H762 V110 H792 V914 H762 V944 H118 V914 H88 V110 H118 Z"
            fill="var(--plaque)"/>
      <path d="M132 96 H748 V124 H776 V900 H748 V928 H132 V900 H104 V124 H132 Z"
            fill="none" stroke="var(--cream)" stroke-width="5"/>
      <path d="M142 106 H738 V134 H766 V890 H738 V918 H142 V890 H114 V134 H142 Z"
            fill="var(--panel)"/>
      <path d="M150 114 H730 V142 H758 V882 H730 V910 H150 V882 H122 V142 H150 Z"
            fill="none" stroke="var(--cream)" stroke-width="2"/>
    </svg>

    <h2 class="category">TUGA DISTILLED GIN</h2>

    <div class="ornament ornament-top" role="img" aria-label="Decorative scrollwork flourishes above the brand name"></div>

    <div class="sun-mark"></div>
    <div class="rule rule-top"></div>
    <h1 class="brand-name">VELMORA</h1>
    <div class="rule rule-bottom"></div>

    <p class="handcrafted">HANDCRAFTED</p>
    <p class="slogan">Distilled in the glow of the<br>Portuguese Sunset</p>

    <div class="ornament ornament-bottom" role="img" aria-label="Decorative scrollwork flourishes below the slogan"></div>

    <div class="fill-in">
      <span class="fill-in-field">Date distilled <span class="fill-in-line"></span></span>
      <span class="fill-in-field">Distiller <span class="fill-in-line"></span></span>
      <span class="fill-in-field">Bottle No. <span class="fill-in-line"></span></span>
      <span class="fill-in-field">Batch No. <span class="fill-in-line"></span></span>
    </div>

    <p class="spec spec-abv">43% vol.</p>
    <p class="spec spec-volume">70 cl</p>
  </section>
</div>
</body>
</html>
```